Training Course Info Brochure

Hi there, I'm looking for a design for A4 Flyer (2-3 pages) on our new Course - Infection Control. I have included a previous brochure on our courses so the designed can see the look and feel we are looking for.

As this is about Infection Control, I would also like to see some RED in the design or wording.

The brochure will need to include quite a few industry/ government logos as well and graphics are important. I have included some (Health Care Industry workers) and am also open to other graphics.

Thanks for considering!

Target Market(s)

The Health profession and students wanting to work in the health field

Industry/Entity Type

Health Care

Font styles to use
Sans Serif

Colors
3277b5
f78f20
ffffff
ec1f27

Requirements
Must have
• Similar feel to the brochure I have included in this brief.

SOME RED lettering as we are teaching Infection Control during the COVID19 pandemic
Nice to have
• Lovely design with quite a few photos graphics

Company details:

Carrow Academy of Learning
RTO 73648
FREECALL : 1800 437 982
www.carrowlearning.edu.au
info@carrowlearning.edu.au

```html
<!DOCTYPE html>
<html lang="en">
<head>
<meta charset="utf-8">
<title>Infection Control Skill Set – Carrow Academy of Learning</title>
<link href="https://fonts.googleapis.com/css2?family=Jost:wght@400;500&family=Jura:wght@500;600&family=Comfortaa:wght@300&display=swap" rel="stylesheet">
<style>
  :root{
    --blue:#3277b5;
    --orange:#f78f20;
    --red:#ec1f27;
    --white:#ffffff;
    --ink:#1a1a1a;
    --badge:#d9dcdf;
  }
  *{box-sizing:border-box;margin:0;padding:0}
  html,body{width:848px;height:1200px;overflow:hidden;background:var(--white)}
  body{font-family:'Jost',sans-serif;color:var(--ink);position:relative}
  .page{position:relative;width:848px;height:1200px;overflow:hidden}
  .heading{font-family:'Jura',sans-serif;font-weight:600;letter-spacing:.3px;position:absolute;white-space:nowrap;z-index:2}
  .heading::after{content:"";position:absolute;left:0;bottom:-8px;width:25px;height:3px;background:currentColor}
  .heading--orange{color:var(--orange)}
  .heading--blue{color:var(--blue)}
  ul{list-style:none}
  li{position:relative;padding-left:26px}
  li::before{content:"";position:absolute;left:1px;top:.62em;width:4px;height:4px;border-radius:50%;background:currentColor}
  section,aside{position:relative;z-index:2}

  /* skills */
  .skills-title{left:52px;top:46px;font-size:17px}
  .skills-list{position:absolute;left:52px;top:84px;font-size:13.6px;line-height:17.2px;width:450px}
  .partner-logo{position:absolute;left:554px;top:89px;width:90px;height:110px;display:flex;flex-direction:column;align-items:center;justify-content:flex-end;gap:6px}
  .partner-logo .mark{width:34px;height:34px;border-radius:50%;background:var(--orange)}
  .partner-logo .name{font-size:12px;font-weight:500;color:var(--blue);text-align:center;line-height:1.15}
  .booklet{position:absolute;left:679px;top:89px;width:118px;height:109px;background:linear-gradient(120deg,#1e2a2c 0%,#1f3d44 45%,#2e8b8a 80%,#3aa3a3 100%)}

  /* orange band */
  .band{position:absolute;left:0;top:275px;width:848px;height:370px;background:var(--orange);z-index:0}
  .ideal-panel{position:absolute;left:414px;top:325px;width:434px;height:447px;background:var(--orange);border-bottom-left-radius:26px;z-index:0}
  .photo{position:absolute;left:0;top:325px;width:414px;height:276px;background:linear-gradient(100deg,#5f8fb8 0%,#c9d3dc 40%,#ece8e4 70%,#f4f2ef 100%);z-index:1}
  .ideal-title{left:432px;top:356px;font-size:19px}
  .ideal-intro{position:absolute;left:432px;top:396px;width:370px;font-size:12.6px;font-weight:500;line-height:18.6px;color:var(--ink)}
  .ideal-lead{position:absolute;left:432px;top:458px;width:370px;font-size:14.2px;line-height:20px;color:var(--white)}
  .ideal-list{position:absolute;left:432px;top:506px;width:368px;font-size:13.2px;line-height:17.1px;color:var(--white)}

  /* job pathways */
  .jobs-title{left:52px;top:686px;font-size:17.5px}
  .jobs-text{position:absolute;left:52px;top:722px;width:356px;font-size:14.6px;line-height:20px}
  .credit-lead{position:absolute;left:52px;top:832px;width:510px;font-size:14.4px;font-weight:500;line-height:20px}
  .credit-list{position:absolute;left:52px;top:882px;width:560px;font-size:14.4px;line-height:20px}
  .more-link{position:absolute;left:52px;top:1078px;width:520px;font-size:14.4px;line-height:21px;color:var(--red)}

  /* partner badges */
  .badge{position:absolute;left:652px;top:862px;width:82px;height:70px;background:var(--badge);border-radius:4px}
  .wordmark{position:absolute;font-family:'Jost',sans-serif;font-weight:500;text-align:center;white-space:nowrap;color:var(--red)}
  .wordmark--hub{left:592px;top:972px;width:200px;font-size:20px;display:flex;align-items:center;gap:8px;justify-content:center}
  .wordmark--hub .mark{width:16px;height:16px;background:var(--red)}
  .wordmark--forward{left:592px;top:1052px;width:200px;font-size:20px}

  /* footer */
  .footer{position:absolute;left:0;top:1148px;width:848px;height:52px;font-family:'Comfortaa',sans-serif;font-weight:300;font-size:11.5px;color:var(--white);z-index:2}
  .footer-contact{position:absolute;left:0;top:0;width:593px;height:52px;background:var(--blue);padding-left:51px;display:flex;align-items:center}
  .footer-web{position:absolute;left:593px;top:0;width:255px;height:52px;background:var(--orange);padding-right:51px;display:flex;align-items:center;justify-content:flex-end}
</style>
</head>
<body>
<main class="page">

  <div class="band"></div>
  <div class="ideal-panel"></div>
  <div class="photo" role="img" aria-label="Photo of a smiling care worker handing a glass of water to an elderly woman in a wheelchair"></div>

  <section class="skills">
    <h2 class="heading heading--orange skills-title">Gain these skills</h2>
    <ul class="skills-list">
      <li>Gain Industry Certification in Hand Hygiene</li>
      <li>Gain Industry Certification in COVID19 Infection Control</li>
      <li>Gain Industry Certification in Cleaning, Disinfection and Sterilisation</li>
      <li>Using personal protective equipment safely (practical session with complimentary PPE samples)</li>
      <li>Understanding the chain of infection</li>
      <li>Identify infection hazards and assess risks</li>
      <li>How to prevent the spread and transmission of infection</li>
      <li>Maintaining a clean work environment</li>
    </ul>
    <div class="partner-logo">
      <span class="mark"></span>
      <span class="name">Clean Hands Alliance</span>
    </div>
    <div class="booklet" role="img" aria-label="Cover of a COVID-19 infection control training booklet showing a magnified virus particle"></div>
  </section>

  <section class="ideal">
    <h2 class="heading heading--blue ideal-title">Who this course is ideal for</h2>
    <p class="ideal-intro">The skill set course is most suitable for anyone working the healthcare sector, or those looking to enter employment in the health fields.</p>
    <p class="ideal-lead">This training is for care workers across all health care settings, including:</p>
    <ul class="ideal-list">
      <li>Hospitals</li>
      <li>Primary care</li>
      <li>Medical practices, allied health, GP and specialist clinics</li>
      <li>Aged care (both in residential aged care facilities or with visiting carers at home, including cleaners and cooks)</li>
      <li>Disability (both in residential/shared care facilities or part-time carers in people’s homes, including cleaners and cooks)</li>
      <li>Allied health</li>
      <li>Aboriginal Community Controlled Health Services</li>
      <li>Pharmacies</li>
      <li>Dental practices, including dentists, nurses, cleaners and receptionists</li>
    </ul>
  </section>

  <section class="pathways">
    <h2 class="heading heading--orange jobs-title">Job opportunities and Study Pathways</h2>
    <p class="jobs-text">This course does not lead to a specific job outcome but will be helpful if you are, or would like to work in any of the areas described above. Our training course is designed to make students Job Ready or to enhance their job role.</p>
    <p class="credit-lead">The Units of Competency is a recognised Unit that can be used as a Credit Transfer in Qualifications such as :</p>
    <ul class="credit-list">
      <li>Certificate III Business Administration (Medical)</li>
      <li>Cert III and IV Health Administration</li>
      <li>Cert III in Individual Support (Aging, disability, home and community)</li>
      <li>Cert III in Allied Health Assistance</li>
      <li>Cert III/IV Dental Assisting</li>
      <li>Certificate III in Aboriginal and/or Torres Strait Islander Primary Health Care</li>
      <li>Cert II/III Community Services</li>
      <li>Certificate III in Cleaning Operations</li>
      <li>Cert II and III Health Support Services</li>
    </ul>
    <p class="more-link">More Qualifications that include this Unit of Competency can be found at https://skillsregister.edu.au/Training/Details/HLTINF001</p>
  </section>

  <aside class="partners">
    <div class="badge"></div>
    <div class="wordmark wordmark--hub"><span class="mark"></span>WorkSkills Hub</div>
    <div class="wordmark wordmark--forward">Skill Forward</div>
  </aside>

  <footer class="footer">
    <div class="footer-contact">FREECALL : 1800 437 982 | info@carrowlearning.edu.au</div>
    <div class="footer-web">www.carrowlearning.edu.au</div>
  </footer>

</main>
</body>
</html>
```